Design a banner for "YOUR AD HERE" live sports site

We just need a your ad here banner, with our mail, vorakbox @ pelunet. com and with a nice desing for our site [url removed, login to view] 728x90 and3 00x250

```html
<!DOCTYPE html>
<html lang="en">
<head>
<meta charset="utf-8">
<title>Your Ad Here – Banner Set</title>
<link rel="stylesheet" href="https://fonts.googleapis.com/css2?family=Russo+One&family=Arimo:wght@700&display=swap">
<style>
  :root {
    --canvas: #ffffff;
    --night: #020602;
    --neon: #2fe62f;
    --neon-deep: #0d7a12;
    --chalk: #eef3e2;
    --ball-light: #f4f4f0;
    --ball-dark: #2a2a2a;
  }
  * { margin: 0; padding: 0; box-sizing: border-box; }
  html, body {
    width: 1200px; height: 600px; overflow: hidden;
    background: var(--canvas);
  }
  .canvas { position: relative; width: 1200px; height: 600px; }

  .banner {
    position: absolute;
    overflow: hidden;
    background: var(--night);
  }
  .banner-leaderboard { left: 54px; top: 22px; width: 1092px; height: 135px; }
  .banner-rectangle { left: 387px; top: 172px; width: 450px; height: 375px; }

  .energy-backdrop { position: absolute; inset: 0; }
  .banner-leaderboard .energy-backdrop {
    background:
      radial-gradient(ellipse 140px 60px at 160px 60px, rgba(47,230,47,.35), transparent 70%),
      radial-gradient(ellipse 90px 140px at 490px 70px, rgba(47,230,47,.75), transparent 70%),
      radial-gradient(ellipse 260px 80px at 330px 90px, rgba(13,122,18,.55), transparent 75%),
      linear-gradient(90deg, #031a04 0%, var(--night) 45%, var(--night) 100%);
  }
  .banner-rectangle .energy-backdrop {
    background:
      radial-gradient(ellipse 110px 200px at 150px 170px, rgba(47,230,47,.8), transparent 70%),
      radial-gradient(ellipse 160px 90px at 60px 70px, rgba(47,230,47,.45), transparent 72%),
      radial-gradient(ellipse 200px 120px at 110px 330px, rgba(13,122,18,.6), transparent 75%),
      linear-gradient(180deg, #052006 0%, var(--night) 60%, #031403 100%);
  }
  .banner::after {
    content: ""; position: absolute; inset: 0;
    box-shadow: inset 0 0 28px 6px rgba(0,0,0,.85);
    pointer-events: none;
  }

  .headline { position: absolute; inset: 0; z-index: 1; font-weight: 400; }
  .word {
    position: absolute;
    font-family: "Russo One", sans-serif;
    font-size: 110px;
    line-height: 1;
    color: var(--chalk);
    white-space: nowrap;
    transform: scaleX(0.72);
    transform-origin: left top;
    text-shadow: 0 0 6px rgba(0,0,0,.9);
  }
  .word.accent { color: var(--neon); }

  .ball {
    position: absolute;
    border-radius: 50%;
    background: radial-gradient(circle at 38% 35%, var(--ball-light) 0%, #cfcfcf 55%, var(--ball-dark) 100%);
  }

  /* 728x90 leaderboard */
  .banner-leaderboard .word { top: 1px; }
  .banner-leaderboard .word-y    { left: 441px; }
  .banner-leaderboard .word-ur   { left: 576px; }
  .banner-leaderboard .word-ad   { left: 720px; }
  .banner-leaderboard .word-here { left: 864px; }
  .banner-leaderboard .ball { left: 487px; top: 8px; width: 90px; height: 90px; }

  /* 300x250 rectangle */
  .banner-rectangle .word { font-size: 109px; }
  .banner-rectangle .word-y    { left: 187px; top: 33px; }
  .banner-rectangle .word-ur   { left: 318px; top: 33px; }
  .banner-rectangle .word-ad   { left: 252px; top: 125px; }
  .banner-rectangle .word-here { left: 201px; top: 211px; }
  .banner-rectangle .ball { left: 230px; top: 41px; width: 88px; height: 88px; }

  .contact {
    position: absolute;
    font-family: "Arimo", sans-serif;
    font-weight: 700;
    color: #ffffff;
    white-space: nowrap;
    line-height: 1;
    z-index: 1;
  }
  .banner-leaderboard .contact { left: 654px; top: 100px; font-size: 21px; }
  .banner-rectangle .contact { left: 178px; top: 314px; font-size: 22px; }
</style>
</head>
<body>
<div class="canvas">

  <section class="banner banner-leaderboard" aria-label="728 by 90 advertising banner">
    <div class="energy-backdrop" role="img" aria-label="Glowing green energy swirls on a dark background"></div>
    <h1 class="headline" aria-label="Your ad here">
      <span class="word word-y">Y</span>
      <span class="ball" role="img" aria-label="Soccer ball"></span>
      <span class="word word-ur">UR</span>
      <span class="word word-ad accent">AD</span>
      <span class="word word-here">HERE</span>
    </h1>
    <p class="contact">vorakbox @ pelunet. com</p>
  </section>

  <section class="banner banner-rectangle" aria-label="300 by 250 advertising banner">
    <div class="energy-backdrop" role="img" aria-label="Glowing green energy swirls on a dark background"></div>
    <h2 class="headline" aria-label="Your ad here">
      <span class="word word-y">Y</span>
      <span class="ball" role="img" aria-label="Soccer ball"></span>
      <span class="word word-ur">UR</span>
      <span class="word word-ad accent">AD</span>
      <span class="word word-here">HERE</span>
    </h2>
    <p class="contact">vorakbox @ pelunet. com</p>
  </section>

</div>
</body>
</html>
```